Modern Business Card For A Digital Advertising Company

I'll be print on the Tarn Prints Velour paper http://us.tarnprints.example/products/velour/business-cards.html
Need's to be modern and use the color palette of the logo or gray scales. I think integrating the pixelation of the logo in to the card and having it wrap from one side to the other could be interesting. My company provides ad operations, web development, and number of other services to websites around the world. You can see my website at http://www.pixelharbor.example
Contact info on the card needs to have
Dana Welloby
President
p.555.318.4406
dana@pixelharbor.example
http://www.pixelharbor.example
Doesn't necessarily need to be in that order
Target Market(s)
Website owners
Industry/Entity Type
Business
Look and feel

```html
<!DOCTYPE html>
<html lang="en">
<head>
<meta charset="utf-8">
<title>Pixel Harbor Business Card</title>
<link rel="stylesheet" href="https://fonts.googleapis.com/css2?family=Great+Vibes&family=Montserrat:wght@400;600;700&display=swap">
<style>
  :root {
    --canvas-bg: #e4e4e4;
    --card-white: #ffffff;
    --brand-green: #8cc63f;
    --ink-dark: #2e2e2e;
    --ink-mid: #555555;
    --card-shadow: 0 6px 18px rgba(0,0,0,0.12);
  }
  * { box-sizing: border-box; margin: 0; padding: 0; }
  html, body {
    width: 1200px; height: 902px; overflow: hidden;
    background: var(--canvas-bg);
  }
  .sheet {
    position: relative; width: 1200px; height: 902px;
    display: flex; align-items: center; justify-content: center; gap: 48px;
  }
  .card {
    position: relative; width: 540px; height: 309px;
    background: var(--card-white); box-shadow: var(--card-shadow);
    overflow: hidden;
  }
  /* Front */
  .card-front .color-field {
    position: absolute; left: 0; top: 0; width: 100%; height: 72%;
    background: var(--brand-green);
  }
  .holder-name {
    position: absolute; left: 150px; top: 92px;
    font-family: "Great Vibes", cursive; font-size: 52px;
    color: var(--card-white); line-height: 1;
  }
  .holder-title {
    position: absolute; left: 298px; top: 146px;
    font-family: "Montserrat", sans-serif; font-weight: 700;
    font-size: 11px; letter-spacing: 0.5px; color: var(--ink-dark);
  }
  .mini-brand {
    position: absolute; right: 18px; top: 196px;
    display: flex; flex-direction: column; align-items: flex-end; gap: 3px;
  }
  .mini-brand .brand-square {
    width: 18px; height: 18px; background: var(--card-white);
    border: 3px solid var(--card-white);
  }
  .mini-brand .brand-name {
    font-family: "Montserrat", sans-serif; font-weight: 600;
    font-size: 7px; letter-spacing: 0.4px; color: var(--brand-green);
    text-transform: uppercase; margin-top: 6px;
  }
  .contact-list {
    position: absolute; left: 18px; bottom: 14px; list-style: none;
    font-family: "Montserrat", sans-serif; font-size: 11px;
    color: var(--ink-mid); line-height: 1.45;
  }
  .contact-list strong { color: var(--ink-dark); font-weight: 700; }
  /* Back */
  .card-back {
    display: flex; align-items: center; justify-content: center;
  }
  .back-brand {
    display: flex; align-items: center; gap: 14px;
  }
  .back-brand .brand-square {
    width: 40px; height: 40px; background: var(--brand-green);
  }
  .back-brand .brand-name {
    font-family: "Montserrat", sans-serif; font-weight: 600;
    font-size: 30px; color: var(--brand-green); letter-spacing: 0.5px;
  }
</style>
</head>
<body>
<main class="sheet">
  <section class="card card-front" aria-label="Business card front">
    <div class="color-field"></div>
    <h1 class="holder-name">Dana Welloby</h1>
    <p class="holder-title">PRESIDENT</p>
    <div class="mini-brand">
      <span class="brand-name">Pixel Harbor</span>
    </div>
    <ul class="contact-list">
      <li>Phone: <strong>555 318 4406</strong></li>
      <li>e-mail: <strong>dana@pixelharbor.example</strong></li>
      <li>http://<strong>www.pixelharbor.example</strong></li>
    </ul>
  </section>
  <section class="card card-back" aria-label="Business card back">
    <div class="back-brand">
      <span class="brand-square"></span>
      <span class="brand-name">Pixel Harbor</span>
    </div>
  </section>
</main>
</body>
</html>
```